Business card design for a dynamic IT consulting company

We need a business card design for a young firm, specialized in the Telecommunications/Consulting industry. The name of the company is Dulmar and Partners Business Consulting Ltd. (Short name: Dulmar and Partnes)
Dulmar = solve read reverse, so we aim to be uncomplicated and solution-oriented. The small pipe in our logo is also related to the word solve. So we need a new business card design, which is simple, eye catching and something non traditional (I would probably prefer a square shaped design rather than a rectangle, but open for suggestions). Attached our logo.

Target Market(s)

Usually our customers are Tier1 Telecoms providers (Q-Linkor, Teravine, etc) and their executives.

Industry/Entity Type

Business

Contact Information for Business Card

Name: Gergely Tarnavedi
Email: g.tarnavedi@dulmar-example.hu
Web: www.dulmar-example.hu
Mobile: +36 30 555 0192
Title: Managing Director

Optional:
Company name: Dulmar and Partners Ltd.
Address: 1021 Budapest, Kovarhegyi str. 17/B, Hungary

Font styles to use
Other font styles liked:
• helveticaneue_medium, Prime Regular are used now.

Colors

Designer to choose colors to be used in the design.

Requirements
Must have
• I would like to have a 2 sided design.
Nice to have
• I thought if we make the logo a bit bigger (without the company name), that could go to the back with the company name below. I though, if the pipe in the logo is somehow touchable on the business card, would be nice and unique.

```html
<!DOCTYPE html>
<html lang="en">
<head>
<meta charset="utf-8">
<title>Dulmar and Partners – Business Card</title>
<link rel="stylesheet" href="https://fonts.googleapis.com/css2?family=Exo+2:wght@400&family=Roboto:wght@400;500;700&display=swap">
<style>
  :root {
    --backdrop: #606060;
    --card-light: #ffffff;
    --card-dark: #39393b;
    --ink: #333333;
    --logo-grey: #58585a;
    --accent-blue: #1e9ad6;
    --accent-magenta: #b0288c;
    --mark-grey: #555557;
  }
  * { margin: 0; padding: 0; box-sizing: border-box; }
  html, body {
    width: 1200px; height: 772px; overflow: hidden;
    background: var(--backdrop);
  }
  .canvas { position: relative; width: 1200px; height: 772px; }

  .card { position: absolute; top: 166px; width: 440px; height: 440px; }
  .card--front { left: 114px; background: var(--card-light); }
  .card--back  { left: 644px; background: var(--card-dark); }

  .wordmark {
    position: absolute;
    font-family: "Exo 2", "Roboto", sans-serif;
    font-weight: 400;
    letter-spacing: -0.5px;
    white-space: nowrap;
    display: flex; align-items: center; gap: 12px;
  }
  .wordmark__square { width: 12px; height: 12px; background: var(--accent-magenta); flex: none; }
  .card--front .wordmark { left: 43px; top: 58px; font-size: 38px; color: var(--logo-grey); }
  .card--back .wordmark {
    left: 0; right: 0; top: 196px; justify-content: center;
    font-size: 40px; color: #ffffff;
  }

  .person { position: absolute; left: 43px; top: 228px; font-family: "Roboto", Arial, sans-serif; color: var(--ink); }
  .person__name { font-size: 22.5px; font-weight: 700; line-height: 1; }
  .person__title { margin-top: 10px; font-size: 15px; color: var(--accent-blue); line-height: 1; }

  .accent-row { position: absolute; left: 43px; top: 294px; display: flex; gap: 15px; }
  .accent-row span { width: 12px; height: 11px; }
  .accent-row .grey { background: var(--mark-grey); }
  .accent-row .blue { background: var(--accent-blue); }
  .accent-row .magenta { background: var(--accent-magenta); }

  .contacts { position: absolute; left: 43px; top: 319px; list-style: none; font-family: "Roboto", Arial, sans-serif; font-size: 15px; color: var(--ink); }
  .contacts li { display: flex; align-items: center; gap: 5px; height: 23px; }
  .contacts svg { width: 17px; height: 17px; flex: none; }
  .contacts strong { font-weight: 700; }
  .address { position: absolute; left: 43px; top: 390px; font-family: "Roboto", Arial, sans-serif; font-size: 15px; color: var(--ink); white-space: nowrap; }
</style>
</head>
<body>
<main class="canvas">
  <section class="card card--front" aria-label="Card front">
    <div class="wordmark"><span class="wordmark__square"></span>Dulmar &amp; Partners</div>

    <div class="person">
      <h1 class="person__name">Gergely Tarnavedi</h1>
      <p class="person__title">Managing Director</p>
    </div>

    <div class="accent-row" aria-hidden="true"><span class="grey"></span><span class="blue"></span><span class="magenta"></span></div>

    <ul class="contacts">
      <li>
        <svg viewBox="0 0 20 20" aria-hidden="true"><circle cx="10" cy="10" r="10" fill="var(--accent-magenta)"/><path d="M4.5 8.5c0-2 2.5-3 5.5-3s5.5 1 5.5 3l-2 .5-.5-1.5h-6L6.5 9z" fill="#fff"/><rect x="6.5" y="10" width="7" height="4.5" rx="1" fill="#fff"/></svg>
        +36 30 555 0192
      </li>
      <li>
        <svg viewBox="0 0 20 20" aria-hidden="true"><circle cx="10" cy="10" r="10" fill="var(--accent-magenta)"/><rect x="5" y="6.5" width="10" height="7" fill="#fff"/><path d="M5 6.5l5 4 5-4" fill="none" stroke="var(--accent-magenta)" stroke-width="1"/></svg>
        g.tarnavedi@dulmar-example.hu
      </li>
      <li>
        <svg viewBox="0 0 20 20" aria-hidden="true"><circle cx="10" cy="10" r="10" fill="var(--accent-magenta)"/><g fill="none" stroke="#fff" stroke-width="1"><circle cx="10" cy="10" r="5.5"/><ellipse cx="10" cy="10" rx="2.4" ry="5.5"/><path d="M4.5 10h11M5.3 7.3h9.4M5.3 12.7h9.4"/></g></svg>
        <span>www.<strong>dulmar-example</strong>.hu</span>
      </li>
    </ul>

    <p class="address">1021 Budapest, Kovarhegyi str. 17/B, Hungary</p>
  </section>

  <section class="card card--back" aria-label="Card back">
    <div class="wordmark">Dulmar &amp; Partners</div>
  </section>
</main>
</body>
</html>
```